Data Management as a Service Powerpoint Design

We need the attached PowerPoint presentation redesigning including all graphics, icons, images, and graphs. The messaging in the content should remain however artistic flair can be used to change any diagram/icon/graph layout.
For preferred colour scheme and brand continuity our website is: velquon.com, however we are open to new colours/scheme.
The only stipulation is that the hexagon layout on the DMaaS product slide (slide 4) must remain. All other icons must be changed. We would also like this to be editable, and not full-slide static images pasted from another graphics suite.

```html
<!DOCTYPE html>
<html lang="en">
<head>
<meta charset="utf-8">
<title>Velquon – Data Management as a Service</title>
<link href="https://fonts.googleapis.com/css2?family=Mulish:wght@400;600;700;800;900&display=swap" rel="stylesheet">
<style>
:root{
  --page:#d9dadc;
  --blue:#0a72bd;
  --blue-dark:#08589a;
  --blue-deep:#063f7c;
  --ink:#333a40;
  --muted:#5b6168;
  --hex-grey:#e8e9eb;
  --white:#ffffff;
  --line:#0a72bd;
}
*{box-sizing:border-box;margin:0;padding:0}
html,body{width:1200px;height:3995px;overflow:hidden}
body{background:var(--page);font-family:"Mulish",sans-serif;color:var(--ink);position:relative}
.slide{position:absolute;left:105px;width:1002px;height:563px;background:var(--white);overflow:hidden}
.slide--cover{top:135px;background:linear-gradient(120deg,#0b5fb0 0%,#0a6ac4 40%,#06397a 100%)}
.slide--application{top:767px}
.slide--services{top:1400px}
.slide--lifecycle{top:2031px}
.slide--assessment{top:2663px}
.slide--closing{top:3296px;background:linear-gradient(135deg,#0a64ad,#0b6bb8 50%,#0a5a9e)}
.slide__floor{position:absolute;left:0;right:0;bottom:45px;height:230px;background:linear-gradient(180deg,rgba(240,241,243,0),#eef0f2)}
.footer{position:absolute;left:0;right:0;bottom:0;height:45px;background:var(--blue);display:flex;align-items:center;justify-content:space-between;padding:0 24px 0 25px;color:var(--white)}
.wordmark{font-weight:800;letter-spacing:3px;color:var(--white)}
.footer .wordmark{font-size:25px}
.footer__section{font-weight:800;font-size:18px}
.hex{position:absolute;clip-path:polygon(25% 0,75% 0,100% 50%,75% 100%,25% 100%,0 50%);display:flex;flex-direction:column;align-items:center;justify-content:center;text-align:center}
.hex--title{background:var(--blue);color:var(--white);font-weight:800;font-size:19px}
/* cover */
.cover__brand{position:absolute;left:65px;top:36px;font-size:44px}
.cover__title{position:absolute;left:65px;top:195px;color:var(--white);font-weight:800;font-size:50px;line-height:60px}
.cover__visual{position:absolute;right:0;top:0;width:560px;height:100%;background:radial-gradient(circle at 70% 40%,rgba(120,200,255,.45),rgba(10,90,170,0) 60%),linear-gradient(90deg,rgba(10,100,190,0),rgba(20,110,200,.5))}
/* application */
.app__title{left:57px;top:36px;width:137px;height:153px}
.app__heading{position:absolute;left:194px;top:71px;width:191px;height:79px;border-top:2px solid var(--line);border-bottom:2px solid var(--line);padding-left:30px;display:flex;align-items:center;color:var(--blue);font-weight:800;font-size:26px}
.shadow-wrap{position:absolute;filter:drop-shadow(0 8px 14px rgba(0,0,0,.08))}
.hex--tile{position:relative;width:186px;height:200px;background:var(--white);color:var(--blue);font-size:16px;font-weight:600;gap:10px}
/* services */
.hex--small{width:136px;height:146px;background:var(--hex-grey);color:var(--ink);font-size:13px;gap:8px;line-height:1.25}
.hex--center{width:183px;height:185px;background:var(--blue);color:var(--white);font-size:16px;gap:10px}
/* lifecycle */
.life__title{left:33px;top:28px;width:157px;height:155px}
.silo-visual{position:absolute;left:122px;top:200px;width:268px;height:188px;border-radius:60px 60px 20px 20px;background:radial-gradient(circle at 50% 40%,#cfe6f8,#5aa8e2 70%,#3a8fd3)}
.label{position:absolute;text-align:center;font-size:16px;color:var(--ink);line-height:1.2}
.arrow{position:absolute;top:274px;color:var(--blue);font-size:20px}
.step-icon{position:absolute}
.storage-box{position:absolute;left:789px;top:184px;width:177px;height:273px;border:2px solid var(--blue);display:flex;flex-direction:column;align-items:center;justify-content:center;gap:18px}
/* assessment */
.assess__title{left:33px;top:52px;width:157px;height:155px}
.dash{position:absolute;background:linear-gradient(90deg,#3a3d41 0 22%,#f4f4f5 22%);border:3px solid #c9cbce}
.list-head{position:absolute;font-weight:800;font-size:16px;color:var(--ink)}
.bullets{position:absolute;list-style:none}
.bullets li{position:relative;padding-left:23px;font-size:15.5px;line-height:23px;margin-bottom:21px;color:var(--ink)}
.bullets li::before{content:"";position:absolute;left:0;top:7px;width:10px;height:10px;border-radius:50%;background:var(--blue)}
.radar{position:absolute;left:735px;top:267px;width:242px;height:222px;background:#eeeff1}
/* closing */
.closing__texture{position:absolute;inset:0;background:radial-gradient(circle at 20% 30%,rgba(120,190,240,.25),transparent 45%),radial-gradient(circle at 80% 70%,rgba(120,190,240,.2),transparent 50%)}
.closing__title{position:absolute;left:368px;top:188px;width:266px;height:88px;border-top:3px solid var(--white);border-bottom:3px solid var(--white);display:flex;align-items:center;justify-content:center;color:var(--white);font-weight:800;font-size:50px}
.closing__brand{position:absolute;left:0;right:0;top:486px;text-align:center;font-size:28px}
</style>
</head>
<body>

<!-- Cover -->
<section class="slide slide--cover">
  <div class="cover__visual" role="img" aria-label="Glowing blue financial chart with candlesticks and a dotted line graph"></div>
  <div class="wordmark cover__brand">VELQUON</div>
  <h1 class="cover__title">Data<br>Management<br>as a Service</h1>
</section>

<!-- Application -->
<section class="slide slide--application">
  <div class="slide__floor"></div>
  <div class="hex hex--title app__title">DMaaS</div>
  <div class="app__heading">Application</div>
  <div class="shadow-wrap" style="left:177px;top:241px">
    <div class="hex hex--tile">
      <svg width="48" height="48" viewBox="0 0 48 48" fill="none" stroke="#0a72bd" stroke-width="2"><circle cx="24" cy="14" r="7"/><circle cx="24" cy="14" r="2.5"/><path d="M24 21v8M10 29h28M10 29v6M24 29v6M38 29v6"/><rect x="6" y="35" width="8" height="6"/><rect x="20" y="35" width="8" height="6"/><rect x="34" y="35" width="8" height="6"/></svg>
      Automation
    </div>
  </div>
  <div class="shadow-wrap" style="left:408px;top:206px">
    <div class="hex hex--tile">
      <svg width="56" height="48" viewBox="0 0 56 48" fill="none" stroke="#0a72bd" stroke-width="2"><text x="20" y="20" font-family="Mulish" font-weight="800" font-size="15" fill="#0a72bd" stroke="none">AI</text><path d="M8 8h6M8 14h4M44 8h-6M46 14h-4M6 34c8 0 12 4 18 4h14c3 0 3-5 0-5H28M6 42h30l14-10c2-2 0-5-3-3l-9 5"/></svg>
      AI
    </div>
  </div>
  <div class="shadow-wrap" style="left:662px;top:156px">
    <div class="hex hex--tile">
      <svg width="48" height="48" viewBox="0 0 48 48" fill="none" stroke="#0a72bd" stroke-width="2"><circle cx="24" cy="24" r="17"/><circle cx="24" cy="24" r="11" stroke-dasharray="4 3"/><circle cx="24" cy="21" r="4"/><path d="M17 32c2-4 12-4 14 0"/></svg>
      Service
    </div>
  </div>
  <footer class="footer"><span class="wordmark">VELQUON</span><span class="footer__section">DMaaS</span></footer>
</section>

<!-- DMaaS services -->
<section class="slide slide--services">
  <div class="slide__floor"></div>
  <div class="hex hex--small" style="left:421px;top:15px">
    <svg width="26" height="30" viewBox="0 0 26 30"><path d="M3 2h14l6 6v20H3z" fill="#2d3238"/><path d="M7 13h12M7 18h12M7 23h8" stroke="#fff" stroke-width="2"/></svg>EDRMS</div>
  <div class="hex hex--small" style="left:287px;top:98px">
    <svg width="34" height="30" viewBox="0 0 34 30" fill="#2d3238"><rect x="10" y="2" width="14" height="10"/><rect x="2" y="10" width="14" height="10"/><rect x="18" y="14" width="14" height="10"/><path d="M2 24h12v4H2z"/></svg>Data<br>Mapping</div>
  <div class="hex hex--small" style="left:554px;top:98px">
    <svg width="32" height="32" viewBox="0 0 32 32"><path d="M4 4h18v24H4z" fill="#2d3238"/><path d="M8 10h10M8 15h10M8 20h6" stroke="#fff" stroke-width="2"/><circle cx="23" cy="21" r="5" fill="none" stroke="#2d3238" stroke-width="2.5"/><path d="M27 25l4 4" stroke="#2d3238" stroke-width="2.5"/></svg>Assessment</div>
  <div class="hex hex--center" style="left:396px;top:162px">
    <svg width="22" height="22" viewBox="0 0 22 22"><circle cx="11" cy="11" r="7" fill="none" stroke="#fff" stroke-width="4" stroke-dasharray="3.5 2"/><circle cx="11" cy="11" r="3" fill="#fff"/></svg>DMaaS</div>
  <div class="hex hex--small" style="left:287px;top:264px">
    <svg width="34" height="34" viewBox="0 0 34 34" fill="none" stroke="#2d3238" stroke-width="2.5"><path d="M10 6a14 14 0 0 1 18 6M28 24a14 14 0 0 1-18 5M5 22a14 14 0 0 1 1-12"/><rect x="13" y="2" width="6" height="6" fill="#2d3238"/><rect x="26" y="15" width="6" height="6" fill="#2d3238"/><rect x="3" y="22" width="6" height="6" fill="#2d3238"/></svg>Lifecycle</div>
  <div class="hex hex--small" style="left:556px;top:264px">
    <svg width="34" height="30" viewBox="0 0 34 30" fill="#2d3238"><rect x="12" y="2" width="10" height="7"/><path d="M17 9v6M6 15h22M6 15v5M28 15v5" stroke="#2d3238" stroke-width="2"/><rect x="2" y="20" width="9" height="7"/><rect x="23" y="20" width="9" height="7"/></svg>Classification</div>
  <div class="hex hex--small" style="left:421px;top:341px">
    <svg width="36" height="32" viewBox="0 0 36 32" fill="#2d3238"><path d="M11 14a7 7 0 0 1 14 0v3H11z"/><rect x="8" y="14" width="20" height="16" rx="2"/><circle cx="18" cy="22" r="2.5" fill="#fff"/><path d="M2 16h5M29 16h5" stroke="#2d3238" stroke-width="2"/></svg>Privacy</div>
  <footer class="footer"><span class="wordmark">VELQUON</span><span class="footer__section">DMaaS</span></footer>
</section>

<!-- Lifecycle -->
<section class="slide slide--lifecycle">
  <div class="slide__floor"></div>
  <div class="hex hex--title life__title">Lifecycle</div>
  <div class="silo-visual" role="img" aria-label="Illustration of clouds, servers and a settings window representing unstructured data siloes"></div>
  <div class="label" style="left:148px;top:419px;width:214px">Unstructured Data Siloes</div>
  <span class="arrow" style="left:417px">→</span>
  <span class="arrow" style="left:585px">→</span>
  <span class="arrow" style="left:751px">→</span>
  <svg class="step-icon" style="left:484px;top:250px" width="56" height="50" viewBox="0 0 56 50" fill="none" stroke="#0a72bd" stroke-width="2"><path d="M3 2v44"/><path d="M3 47h50" stroke-dasharray="5 3"/><path d="M9 32l10-14 10 10 10-16 10 8"/><circle cx="19" cy="18" r="2"/><circle cx="29" cy="28" r="2"/><circle cx="39" cy="12" r="2"/></svg>
  <div class="label" style="left:452px;top:330px;width:120px">ROT<br>Analysis</div>
  <svg class="step-icon" style="left:645px;top:252px" width="58" height="58" viewBox="0 0 58 58" fill="none" stroke="#0a72bd" stroke-width="2"><circle cx="29" cy="29" r="8" stroke-dasharray="4 2"/><circle cx="29" cy="29" r="3"/><path d="M29 5v13M29 40v13M5 29h13M40 29h13M12 12l9 9M37 37l9 9M46 12l-9 9M12 46l9-9"/><circle cx="29" cy="4" r="3"/><circle cx="29" cy="54" r="3"/><circle cx="4" cy="29" r="3"/><circle cx="54" cy="29" r="3"/><circle cx="11" cy="11" r="3"/><circle cx="47" cy="47" r="3"/><circle cx="47" cy="11" r="3"/><circle cx="11" cy="47" r="3"/></svg>
  <div class="label" style="left:609px;top:330px;width:130px">Automated<br>Remediation</div>
  <div class="label" style="left:772px;top:134px;width:211px">Storage Vendor<br>Agnostic</div>
  <div class="storage-box">
    <svg width="54" height="58" viewBox="0 0 54 58" fill="none" stroke="#0a72bd" stroke-width="2.5"><ellipse cx="27" cy="9" rx="24" ry="7"/><path d="M3 9v40c0 4 11 7 24 7s24-3 24-7V9M3 22c0 4 11 7 24 7s24-3 24-7M3 35c0 4 11 7 24 7s24-3 24-7"/></svg>
    <div style="text-align:center;font-size:16px;line-height:1.2">Streamlined,<br>Controlled Data<br>Storage</div>
  </div>
  <footer class="footer"><span class="wordmark">VELQUON</span><span class="footer__section">DMaaS | Lifecycle</span></footer>
</section>

<!-- Assessment -->
<section class="slide slide--assessment">
  <div class="hex hex--title assess__title">Assessment</div>
  <div class="dash" style="left:248px;top:57px;width:270px;height:155px" role="img" aria-label="Sensitive data assessment dashboard with bar and pie charts"></div>
  <div class="dash" style="left:45px;top:254px;width:360px;height:208px" role="img" aria-label="Data age assessment dashboard with bar charts and inactive data analysis"></div>
  <div class="list-head" style="left:572px;top:48px">PACKAGED</div>
  <ul class="bullets" style="left:572px;top:86px;width:400px">
    <li>Data centric storage refresh or cloud migration readiness assessment</li>
    <li>Data Owner and Data Access Assessment</li>
    <li>Data Classification and Sensitivity Assessment</li>
  </ul>
  <div class="list-head" style="left:448px;top:340px">GENERIC</div>
  <ul class="bullets" style="left:448px;top:377px;width:280px">
    <li>Data Management Assessment</li>
  </ul>
  <svg class="radar" viewBox="0 0 242 222">
    <g fill="none" stroke="#b9bcc0" stroke-width="1">
      <polygon points="121,28 211,111 121,194 31,111"/>
      <polygon points="121,56 181,111 121,166 61,111"/>
      <polygon points="121,84 151,111 121,138 91,111"/>
      <path d="M121 28v166M31 111h180"/>
    </g>
    <polygon points="121,38 191,111 121,141 91,111" fill="rgba(160,40,40,.15)" stroke="#a33a3a" stroke-width="2"/>
    <polygon points="121,50 180,111 121,150 105,111" fill="none" stroke="#d49a9a" stroke-width="1.5"/>
    <g fill="#8b1d1d"><circle cx="121" cy="38" r="4"/><circle cx="191" cy="111" r="4"/><circle cx="121" cy="141" r="4"/></g>
    <g font-family="Mulish" font-size="9" fill="#555" text-anchor="middle"><text x="121" y="20">Security</text><text x="121" y="210">Compliance</text><text x="20" y="114">Storage</text><text x="224" y="114">Usage</text></g>
  </svg>
  <footer class="footer"><span class="wordmark">VELQUON</span><span class="footer__section">DMaaS | Assessment</span></footer>
</section>

<!-- Closing -->
<section class="slide slide--closing">
  <div class="closing__texture" role="img" aria-label="Faint network mesh texture on blue"></div>
  <div class="closing__title">Thank You</div>
  <div class="wordmark closing__brand">VELQUON</div>
</section>

</body>
</html>
```